Website redesign

We need a bold revamp of our website (http://www.brantocksparkworks.co.nz/)
which at the moment looks dated. We want a crisp, fresh and bold look. The background image behind web page can go. Open to complete new layout

Target Market(s)

Electrical contracting company- working in the domestic and commercial field

Coding

Coded - Design and coding required

Number of Pages Required

5+ page

Font styles to use
Sans Serif

Colors

Designer to choose colors to be used in the design.

```html
<!DOCTYPE html>
<html lang="en">
<head>
<meta charset="utf-8">
<title>Brantock Sparkworks – Electrical Contractors</title>
<link href="https://fonts.googleapis.com/css2?family=Roboto:wght@400;500;700;900&display=swap" rel="stylesheet">
<style>
:root{
  --red:#ee1c24;
  --red-dark:#d0111a;
  --black:#000;
  --ink:#222;
  --grey:#666;
  --light:#f2f2f2;
  --badge:#e4e4e4;
  --white:#fff;
}
*{box-sizing:border-box;margin:0;padding:0}
html,body{width:1200px;height:4523px;overflow:hidden}
body{position:relative;background:var(--white);font-family:"Roboto",Arial,sans-serif;color:var(--ink)}
.abs{position:absolute}
.center{text-align:center;left:0;width:1200px}

/* header */
.brand{left:120px;top:40px}
.brand-name{font-weight:900;font-size:34px;line-height:34px;color:var(--black);letter-spacing:-0.5px}
.header-phone{left:812px;top:58px;display:flex;gap:14px;align-items:center}
.header-phone .nums{font-size:16px;line-height:22px;color:var(--ink)}
.badge{left:1003px;top:38px;width:80px;height:80px;border-radius:50%;background:var(--badge)}

.nav{left:0;top:163px;width:1200px;height:48px;background:var(--red)}
.nav a{position:absolute;top:0;height:48px;line-height:48px;color:var(--white);font-size:15px;font-weight:700;text-decoration:none;padding:0 14px}
.nav a.active{background:var(--black)}

.hero{left:0;top:211px;width:1200px;height:594px;background:linear-gradient(120deg,#c9c9c9,#ecebe8 45%,#9a9a9a 80%,#c0392b)}
.dots{top:828px;left:576px;display:flex;gap:8px}
.dots span{width:9px;height:9px;border-radius:50%;background:#444}
.dots span:first-child{background:var(--red)}

/* services grid */
.svc{width:182px;height:172px;text-align:center;padding-top:38px}
.svc svg{width:58px;height:58px}
.svc p{font-size:24px;color:var(--ink);margin-top:14px;line-height:26px}
.svc.active{background:var(--red);border-radius:4px}
.svc.active p{color:var(--white);font-weight:700}

.btn{display:block;width:114px;height:26px;line-height:26px;border-radius:13px;background:var(--red);color:var(--white);font-size:12px;font-weight:700;text-align:center}

/* dark bands */
.band{left:0;width:1200px;background:var(--black)}
.sec-title{font-size:23px;font-weight:700;color:var(--white)}
.sec-sub{font-size:13px;color:var(--white)}
.dark{color:var(--ink)}
.arrows{left:1022px;top:1444px;display:flex;gap:8px}
.arrows span{width:22px;height:22px;border-radius:50%;border:2px solid var(--white)}
.arrows span.on{background:var(--red);border-color:var(--red)}

.card{width:234px;height:316px;background:var(--white)}
.card .ph{height:229px}
.card p{height:87px;display:flex;align-items:center;justify-content:center;text-align:center;font-size:20px;line-height:24px;color:var(--ink);font-weight:500}

.tile{width:232px;height:224px}
.tile-cap{color:var(--white);text-align:center;font-size:24px;font-weight:700;padding-top:130px}
.tile-cap small{display:block;font-size:11px;font-weight:400}

.news{width:311px;height:332px;background:var(--white);padding:9px}
.news .ph{height:187px;position:relative}
.news .date{position:absolute;left:9px;top:9px;width:32px;height:36px;background:var(--red);color:var(--white);font-size:13px;font-weight:700;text-align:center;line-height:15px;padding-top:3px}
.news .date small{display:block;font-size:9px;font-weight:400}
.news h4{color:var(--red);font-size:13px;font-weight:700;margin-top:12px}
.news .meta{font-size:11px;color:var(--grey);margin:3px 0 6px;display:flex;justify-content:space-between}
.news .txt{font-size:12px;line-height:16px;color:var(--ink)}
.news .more{font-size:12px;color:var(--ink);margin-top:6px}

.partner{width:278px;height:121px;background:var(--light);display:flex;align-items:center;justify-content:center}
.partner span{width:180px;height:50px;background:#d8d8d8}

.welcome-txt{left:220px;top:3713px;width:760px;text-align:center;font-size:14px;line-height:23px;color:var(--ink)}

.sub-form{left:301px;top:4067px;width:561px;height:28px;border-bottom:1px solid #ccc;display:flex}
.sub-form .in{flex:1;font-size:12px;color:var(--grey);line-height:28px;padding-left:6px}
.sub-form .go{width:123px;background:var(--red);color:var(--white);font-size:14px;font-weight:700;text-align:center;line-height:28px;border-radius:0 14px 14px 0}

/* footer */
.footer{left:0;top:4161px;width:1200px;height:362px;background:var(--red)}
.f-logo{left:84px;top:4227px;width:233px;height:106px;background:var(--white);display:flex;align-items:center;justify-content:center}
.f-about{left:120px;top:4350px;width:220px;font-size:13px;line-height:17px;font-weight:700;color:var(--white)}
.f-head{font-size:13px;font-weight:700;color:var(--white);text-transform:uppercase}
.f-head::after{content:"";display:block;width:26px;height:2px;background:var(--white);margin-top:5px}
.f-links{list-style:none;font-size:13px;font-weight:700;color:var(--white);line-height:27px}
.f-links li::before{content:"• "}
.f-contact{font-size:13px;font-weight:700;color:var(--white);line-height:27px}
.f-contact div{display:flex;gap:10px;align-items:center}
.f-contact svg{width:14px;height:14px;fill:var(--white)}
.f-field{height:24px;background:var(--red-dark);border:1px solid #ff5a5f;color:var(--white);font-size:11px;padding:4px 8px}
.f-send{width:144px;height:26px;border-radius:13px;background:var(--black);color:var(--white);font-size:12px;font-weight:700;text-align:center;line-height:26px}
.f-bottom{left:0;top:4477px;width:1200px;height:46px;border-top:1px solid #ff5a5f}
.f-copy{left:120px;top:4493px;font-size:12px;font-weight:700;color:var(--white)}
.f-social{left:916px;top:4487px;display:flex;gap:8px}
.f-social span{width:24px;height:24px;border-radius:50%;background:var(--white)}
</style>
</head>
<body>

<!-- header -->
<div class="abs brand">
  <div class="brand-name">Brantock<br>Sparkworks</div>
</div>
<div class="abs header-phone">
  <svg width="22" height="38" viewBox="0 0 22 38"><rect x="2" y="2" width="18" height="34" rx="3" fill="none" stroke="#ee1c24" stroke-width="3"/><circle cx="11" cy="30" r="2" fill="#ee1c24"/></svg>
  <div class="nums">0800 46 71 52<br>(06) 512 7730</div>
</div>
<div class="abs badge"></div>

<nav class="abs nav">
  <a class="active" style="left:120px">Home</a>
  <a style="left:222px">About Us</a>
  <a style="left:338px">Services</a>
  <a style="left:452px">Projects</a>
  <a style="left:566px">Contact Us</a>
  <a style="left:694px">Info</a>
</nav>

<div class="abs hero" role="img" aria-label="Close-up of a hand testing a switchboard of circuit breakers with a red probe"></div>
<div class="abs dots"><span></span><span></span><span></span><span></span></div>

<!-- service icons -->
<div class="abs svc" style="left:81px;top:889px">
  <svg viewBox="0 0 58 58"><circle cx="29" cy="29" r="22" fill="none" stroke="#222" stroke-width="3"/><path d="M32 12 20 31h9l-3 15 12-20h-9z" fill="#222"/></svg>
  <p>Electrical</p>
</div>
<div class="abs svc active" style="left:371px;top:889px">
  <svg viewBox="0 0 58 58"><rect x="8" y="8" width="42" height="42" rx="4" fill="none" stroke="#fff" stroke-width="3"/><line x1="8" y1="19" x2="50" y2="19" stroke="#fff" stroke-width="3"/><circle cx="16" cy="13.5" r="2" fill="#fff"/><circle cx="24" cy="13.5" r="2" fill="#fff"/><rect x="15" y="25" width="28" height="18" rx="2" fill="none" stroke="#fff" stroke-width="3"/></svg>
  <p>Appliances</p>
</div>
<div class="abs svc" style="left:663px;top:889px">
  <svg viewBox="0 0 58 58"><path d="M18 40V26a11 11 0 0 1 22 0v14z" fill="none" stroke="#222" stroke-width="3"/><line x1="12" y1="41" x2="46" y2="41" stroke="#222" stroke-width="3"/><path d="M25 46a4 4 0 0 0 8 0" fill="none" stroke="#222" stroke-width="3"/><path d="M8 18l5 4M50 18l-5 4M29 5v6" stroke="#222" stroke-width="3"/></svg>
  <p>Alarms</p>
</div>
<div class="abs svc" style="left:940px;top:889px">
  <svg viewBox="0 0 58 58"><path d="M29 6 48 13v15c0 12-8 20-19 24C18 48 10 40 10 28V13z" fill="none" stroke="#222" stroke-width="3"/><rect x="21" y="28" width="16" height="12" rx="2" fill="#222"/><path d="M24 28v-4a5 5 0 0 1 10 0v4" fill="none" stroke="#222" stroke-width="3"/></svg>
  <p>Security</p>
</div>
<div class="abs svc" style="left:81px;top:1100px">
  <svg viewBox="0 0 58 58"><circle cx="29" cy="29" r="22" fill="none" stroke="#222" stroke-width="3"/><path d="M17 22c4-4 8 4 12 0s8 4 12 0M17 30c4-4 8 4 12 0s8 4 12 0M17 38c4-4 8 4 12 0s8 4 12 0" fill="none" stroke="#222" stroke-width="3"/></svg>
  <p>Heat Pumps</p>
</div>
<div class="abs svc" style="left:367px;top:1100px">
  <svg viewBox="0 0 58 58"><path d="M29 5c2 10 14 16 14 30a14 14 0 0 1-28 0c0-8 5-12 7-16 2 5 4 7 6 8 2-8-1-16 1-22z" fill="#222"/></svg>
  <p>Fire / Smoke</p>
</div>
<div class="abs svc" style="left:663px;top:1100px">
  <svg viewBox="0 0 58 58"><rect x="16" y="6" width="26" height="46" fill="#222"/><g fill="#fff"><rect x="21" y="12" width="5" height="5"/><rect x="32" y="12" width="5" height="5"/><rect x="21" y="22" width="5" height="5"/><rect x="32" y="22" width="5" height="5"/><rect x="21" y="32" width="5" height="5"/><rect x="32" y="32" width="5" height="5"/><rect x="26" y="42" width="6" height="10"/></g></svg>
  <p style="line-height:24px">BWOF Building<br>Compliance</p>
</div>
<div class="abs svc" style="left:940px;top:1100px">
  <svg viewBox="0 0 58 58"><rect x="17" y="4" width="24" height="50" rx="4" fill="none" stroke="#222" stroke-width="3"/><line x1="17" y1="12" x2="41" y2="12" stroke="#222" stroke-width="3"/><line x1="17" y1="44" x2="41" y2="44" stroke="#222" stroke-width="3"/><circle cx="29" cy="49" r="2" fill="#222"/></svg>
  <p>Phone / Data</p>
</div>
<span class="abs btn" style="left:537px;top:1295px">Read More</span>

<!-- our services -->
<section class="abs band" style="top:1396px;height:579px"></section>
<div class="abs center sec-title" style="top:1440px">Our Services</div>
<div class="abs center sec-sub" style="top:1475px">Lorem Ipsum is simply dummy and typesetting industry.</div>
<div class="abs arrows"><span></span><span class="on"></span></div>
<div class="abs card" style="left:121px;top:1529px"><div class="ph" role="img" aria-label="Timber roof framing with new electrical cabling" style="background:linear-gradient(160deg,#8a5a32,#c89a66 60%,#5a3a20)"></div><p>Residential<br>Electrical</p></div>
<div class="abs card" style="left:362px;top:1529px"><div class="ph" role="img" aria-label="Steel ceiling trusses of a commercial building" style="background:linear-gradient(160deg,#8c9096,#dfe3e6 55%,#6d7278)"></div><p>Commercial<br>Electrical</p></div>
<div class="abs card" style="left:603px;top:1529px"><div class="ph" role="img" aria-label="Security camera mounted on a wall against the sky" style="background:linear-gradient(160deg,#4d7fb3,#d8e6f2 55%,#9bb6cf)"></div><p>Kaiwa Heat<br>Pumps</p></div>
<div class="abs card" style="left:847px;top:1529px"><div class="ph" role="img" aria-label="Hot water cylinder and alarm equipment in a utility cupboard" style="background:linear-gradient(160deg,#6b5c50,#d9d4cf 55%,#a33a2c)"></div><p>Fire Alarms</p></div>
<span class="abs btn" style="left:537px;top:1894px">View More</span>

<!-- projects -->
<div class="abs center sec-title dark" style="top:2044px;font-weight:500;font-size:21px">Projects</div>
<div class="abs center sec-sub" style="top:2080px;color:var(--ink)">Lorem Ipsum is simply dummy and typesetting industry.</div>
<div class="abs tile" style="left:121px;top:2147px;background:linear-gradient(180deg,#b8cde0,#a04a3a 55%,#6a6a6a)" role="img" aria-label="Brick corner shop on a street"></div>
<div class="abs tile" style="left:362px;top:2147px;background:linear-gradient(180deg,#c9d6e0,#4a4a4a 50%,#8a8a8a)" role="img" aria-label="Dark modern commercial building frontage"></div>
<div class="abs tile" style="left:603px;top:2147px;background:linear-gradient(180deg,#a8c4dc,#e8e8e8 50%,#5a7a98)" role="img" aria-label="Retail store with a blue canopy"></div>
<div class="abs tile" style="left:847px;top:2147px;background:linear-gradient(180deg,#9cc0e0,#f0f0f0 45%,#c8202a 60%,#7a7a7a)" role="img" aria-label="Motorhall car dealership building"></div>
<div class="abs tile" style="left:121px;top:2382px;background:linear-gradient(180deg,#a8b8c8,#8a2a22 50%,#6a6a6a)" role="img" aria-label="Red trimmed shopfront on a corner"></div>
<div class="abs tile" style="left:362px;top:2382px;background:linear-gradient(180deg,#3a3a3a,#5a5a5a)" role="img" aria-label="Veterinary clinic building at dusk"><div class="tile-cap">Vets on Marlow 2<small>Project Name - Ravenport</small></div></div>
<div class="abs tile" style="left:603px;top:2382px;background:linear-gradient(180deg,#2a4a8a,#d02030 45%,#8a8a8a)" role="img" aria-label="Denim Lane clothing store frontage"></div>
<div class="abs tile" style="left:847px;top:2382px;background:linear-gradient(180deg,#2e6fc0,#cfe0f0 50%,#5a8a3a 70%)" role="img" aria-label="Grandstand beside a sports field"></div>
<span class="abs btn" style="left:537px;top:2654px">View More</span>

<!-- news -->
<section class="abs band" style="top:2744px;height:582px"></section>
<div class="abs center sec-title" style="top:2803px">NEWS</div>
<div class="abs center sec-sub" style="top:2832px">Lorem Ipsum is simply dummy text.</div>
<div class="abs arrows" style="top:2806px"><span></span><span class="on"></span></div>

<div class="abs news" style="left:108px;top:2879px">
  <div class="ph" role="img" aria-label="Wall mounted heat pump unit" style="background:linear-gradient(160deg,#bfbfbf,#f4f4f4 60%,#c8c8c8)"><div class="date">04<small>Feb</small></div></div>
  <h4>POST TITLE</h4>
  <div class="meta"><span>February 26, 2018</span><span>♡ 20 &nbsp; ▢ 12</span></div>
  <div class="txt">Lorem Ipsum is simply dummy text of the and printing matter and typesetting industry.</div>
  <div class="more">Read More..</div>
</div>
<div class="abs news" style="left:440px;top:2879px">
  <div class="ph" role="img" aria-label="Electrician in a hard hat working at a switchboard" style="background:linear-gradient(160deg,#d8e4ee,#4f7fb8 60%,#e8e0d0)"><div class="date">10<small>Feb</small></div></div>
  <h4>POST TITLE</h4>
  <div class="meta"><span>February 24, 2018</span><span>♡ 20 &nbsp; ▢ 12</span></div>
  <div class="txt">Lorem Ipsum is simply dummy text of the printing and typesetting industry.</div>
  <div class="more">Read More..</div>
</div>
<div class="abs news" style="left:772px;top:2879px">
  <div class="ph" role="img" aria-label="Security camera on a glass building" style="background:linear-gradient(160deg,#6a8ab0,#dfe8f0 55%,#8aa4c0)"><div class="date">22<small>Feb</small></div></div>
  <h4>POST TITLE</h4>
  <div class="meta"><span>February 22, 2018</span><span>♡ 20 &nbsp; ▢ 12</span></div>
  <div class="txt">Lorem Ipsum is simply dummy text of the printing and typesetting industry.</div>
  <div class="more">Read More..</div>
</div>
<span class="abs btn" style="left:537px;top:3263px">View More</span>

<!-- partners -->
<div class="abs center" style="top:3388px;font-size:24px;font-weight:700;color:var(--ink)">WE ARE AUTHORISED INSTALLERS FOR</div>
<div class="abs partner" style="left:307px;top:3452px"><span></span></div>
<div class="abs partner" style="left:615px;top:3452px"><span></span></div>

<!-- welcome -->
<div class="abs center" style="top:3654px;font-size:18px;color:var(--ink)">Welcome</div>
<div class="abs" style="left:580px;top:3682px;width:40px;height:2px;background:var(--red)"></div>
<p class="abs welcome-txt">Brantock Sparkworks is a leading electrical installation and maintenance company based in Ravenport, but servicing all New Zealand. With over 15 professionally qualified and experienced Ravenport electricians, technicians and support staff we are leading the way in providing quality electrical services. Brantock Sparkworks was established in 1991 and does it all, from supplying and changing light bulbs, comprehensive whole house electrical design and installation, to commercial and large scale industrial consultation, implementation and servicing.</p>
<span class="abs btn" style="left:537px;top:3891px">Read More</span>

<!-- newsletter -->
<div class="abs center" style="top:3986px;font-size:22px;font-weight:700;color:var(--ink)">SUBSCRIBE TO OUR NEWSLETTER</div>
<div class="abs center" style="top:4016px;font-size:15px;color:var(--ink)">to receive the latest news &amp; update</div>
<div class="abs sub-form"><div class="in">Your Email</div><div class="go">SUBMIT</div></div>

<!-- footer -->
<footer class="abs footer"></footer>
<div class="abs f-logo"><div class="brand-name" style="font-size:30px;line-height:30px">Brantock<br>Sparkworks</div></div>
<p class="abs f-about">Lorem Ipsum is simply dummy text of the printing and typesetting Lorem Ipsum industry.</p>

<div class="abs f-head" style="left:392px;top:4227px">Quick Link</div>
<ul class="abs f-links" style="left:400px;top:4263px">
  <li>Home</li><li>About Us</li><li>Services</li><li>Projects</li><li>Contact Us</li><li>Info</li>
</ul>

<div class="abs f-head" style="left:534px;top:4227px">Contact Us</div>
<div class="abs f-contact" style="left:534px;top:4263px">
  <div><svg viewBox="0 0 14 14"><path d="M7 0a5 5 0 0 0-5 5c0 4 5 9 5 9s5-5 5-9a5 5 0 0 0-5-5zm0 7a2 2 0 1 1 0-4 2 2 0 0 1 0 4z"/></svg><span>: &nbsp;14 Harlow Street,</span></div>
  <div><span style="width:14px"></span><span>&nbsp; &nbsp;Ravenport 4820</span></div>
  <div><svg viewBox="0 0 14 14"><path d="M3 0h3l1 4-2 1a8 8 0 0 0 4 4l1-2 4 1v3c0 1-1 2-2 2C5 13 1 9 1 2c0-1 1-2 2-2z"/></svg><span>: &nbsp;0800 46 71 52</span></div>
  <div><svg viewBox="0 0 14 14"><path d="M3 0h3l1 4-2 1a8 8 0 0 0 4 4l1-2 4 1v3c0 1-1 2-2 2C5 13 1 9 1 2c0-1 1-2 2-2z"/></svg><span>: &nbsp;(06) 512 7730</span></div>
  <div><svg viewBox="0 0 14 14"><rect x="1" y="2" width="12" height="10" rx="1"/></svg><span>: &nbsp;(06) 512 7731</span></div>
  <div><svg viewBox="0 0 14 14"><path d="M0 2h14v10H0z"/></svg><span>: &nbsp;office@brantockspark.co.nz</span></div>
</div>

<div class="abs f-head" style="left:805px;top:4227px">Quick Contact</div>
<div class="abs f-field" style="left:805px;top:4274px;width:138px">Name</div>
<div class="abs f-field" style="left:948px;top:4274px;width:126px">Phone</div>
<div class="abs f-field" style="left:805px;top:4306px;width:269px;height:62px">Message</div>
<div class="abs f-send" style="left:930px;top:4391px">SEND</div>

<div class="abs f-bottom"></div>
<div class="abs f-copy">Copyright 2018 Brantock Sparkworks. All Rights Reserved.</div>
<div class="abs f-social"><span></span><span></span><span></span><span></span><span></span></div>

</body>
</html>
```